Billboard design for dentist that sees only children

I own a 12' x 25' digital billboard and I need help with billboard design. My wife is a general dentist that only sees children and is very passionate about giving them a quality dental experience . She has a great reputation in town. Obviously with a billboard there can't be a lot of reading. Maybe something that shows safety, love, experience and children. I am completely open to your ideas. In addition I have other businesses that also need billboard design so this could lead to more work. If you go to Maplecovedental.com under the about section you will find more information about the practice and our phone number. Attached is our logo which could be changed and content specs for the digital billboard. Happy Designing!!

Target Market(s)

Parents with children

Colors

Designer to choose colors to be used in the design.

Requirements
Must have
• Must attract attention and be nice to look at.
Nice to have
• Probably should have children in the picture ..... Maybe
Should not have
• If I see something I don't like I will let you know

```html
<!DOCTYPE html>
<html lang="en">
<head>
<meta charset="utf-8">
<title>Maple Cove Dental – Billboard</title>
<link href="https://fonts.googleapis.com/css2?family=Bitter:wght@400;700;800&display=swap" rel="stylesheet">
<style>
  :root {
    --stage: #3c3d40;
    --sky-blue: #0895f5;
    --sky-glow: #8ed3ff;
    --white: #ffffff;
    --brand-green: #2f6e52;
    --cta-green: #0e8f3c;
    --skin: #f1c7a6;
    --towel: #3a9ad6;
  }
  * { box-sizing: border-box; margin: 0; padding: 0; }
  html, body {
    width: 1200px; height: 1200px; overflow: hidden;
    background: var(--stage);
  }
  .canvas {
    position: relative; width: 1200px; height: 1200px;
  }
  .billboard {
    position: absolute; left: 40px; top: 335px;
    width: 1120px; height: 530px;
    background: var(--sky-blue);
    overflow: hidden;
    font-family: "Bitter", Georgia, serif;
    color: var(--white);
  }
  .logo-panel {
    position: absolute; left: 67px; top: 0;
    width: 515px; height: 140px;
    background: var(--white);
    border-radius: 0 0 24px 24px;
    display: flex; align-items: center; gap: 18px;
    padding: 0 26px;
  }
  .logo-dot {
    width: 62px; height: 62px; border-radius: 50%;
    background: var(--brand-green); flex: none;
  }
  .logo-text { color: var(--brand-green); font-weight: 400; }
  .logo-name { font-size: 43px; line-height: 1; }
  .logo-tagline { font-size: 19px; margin-top: 6px; text-align: right; }
  .headline {
    position: absolute; left: 69px; top: 166px;
    font-weight: 800; line-height: 0.86;
    text-transform: uppercase;
  }
  .headline .big { display: block; font-size: 88px; }
  .headline .small { display: block; font-size: 60px; margin-top: 14px; }
  .cta {
    position: absolute; left: 69px; top: 424px;
    width: 492px; height: 66px;
    background: var(--cta-green);
    display: flex; align-items: center; justify-content: center;
    font-weight: 700; font-size: 38px; letter-spacing: 0.5px;
  }
  .cta .label { margin-right: 20px; }
  .photo {
    position: absolute; right: 0; top: 0;
    width: 462px; height: 530px;
    background:
      radial-gradient(ellipse 38% 36% at 50% 45%, var(--skin) 0%, rgba(241,199,166,0.85) 55%, rgba(241,199,166,0) 100%),
      radial-gradient(ellipse 60% 30% at 50% 100%, var(--towel) 0%, rgba(58,154,214,0) 100%),
      radial-gradient(ellipse 60% 60% at 50% 45%, var(--sky-glow) 0%, var(--sky-blue) 100%);
  }
</style>
</head>
<body>
  <div class="canvas">
    <section class="billboard">
      <div class="logo-panel">
        <span class="logo-dot"></span>
        <div class="logo-text">
          <div class="logo-name">Maple Cove Dental</div>
          <div class="logo-tagline">general dentistry for children</div>
        </div>
      </div>
      <h1 class="headline">
        <span class="big">Healthy</span>
        <span class="big">Smiles</span>
        <span class="small">Start Early</span>
      </h1>
      <div class="cta"><span class="label">CALL</span><span class="phone">555-014-2387</span></div>
      <div class="photo" role="img" aria-label="Photo of a smiling young child with a towel around the shoulders holding a toothbrush"></div>
    </section>
  </div>
</body>
</html>
```